Keystone Haulers Billboard design

I need two billboard designs using our logo and adding a few words Looking for a black background with our logo and wording in either purple or white.

need it to have our website keystonehaulers-example.com. phone number 555 201 4387

Also have 16/20/30 yard dumpsters available!

one billboard is size 7x21 feet the other is 15x 21 ft

Target Market(s)

Contractors, home owners

Requirements
Must have
• Use font similar to logo that is eye catching

```html
<!DOCTYPE html>
<html lang="en">
<head>
<meta charset="utf-8">
<title>Keystone Haulers Billboard</title>
<link rel="stylesheet" href="https://fonts.googleapis.com/css2?family=Oswald:wght@600;700&family=Poppins:wght@700;800&display=swap">
<style>
  :root {
    --page: #d6d6d8;
    --board: #050505;
    --purple: #7b3fa8;
    --purple-line: #8a4cc0;
    --shade: #262626;
    --shade-soft: #1a1a1a;
    --white: #ffffff;
  }
  html, body {
    margin: 0;
    width: 1144px;
    height: 1200px;
    overflow: hidden;
    background: var(--page);
  }
  .billboard {
    position: absolute;
    left: 0;
    top: 409px;
    width: 1144px;
    height: 381px;
    display: block;
  }
  .board-bg { fill: var(--board); }
  .divider { fill: var(--white); }
  .deco-dark { fill: var(--shade); }
  .deco-darker { fill: var(--shade-soft); }
  .deco-ring { fill: none; stroke: var(--purple-line); stroke-width: 2; }
  .deco-line { stroke: var(--purple-line); stroke-width: 2; }
  .brand-name {
    font-family: "Poppins", sans-serif;
    font-weight: 800;
    font-size: 50px;
    fill: var(--white);
    letter-spacing: 1px;
  }
  .tagline {
    font-family: "Oswald", sans-serif;
    font-weight: 700;
    font-size: 48px;
    fill: var(--white);
    stroke: var(--purple);
    stroke-width: 2px;
    paint-order: stroke;
  }
  .lead {
    font-family: "Poppins", sans-serif;
    font-weight: 700;
    font-size: 29px;
    fill: var(--white);
    letter-spacing: -0.5px;
  }
  .sizes {
    font-family: "Poppins", sans-serif;
    font-weight: 700;
    font-size: 49px;
    fill: var(--purple);
    letter-spacing: -2px;
  }
  .rule { fill: var(--white); }
  .contact-band { fill: var(--purple); }
  .contact-web {
    font-family: "Oswald", sans-serif;
    font-weight: 600;
    font-size: 21px;
    fill: var(--white);
  }
  .contact-phone {
    font-family: "Oswald", sans-serif;
    font-weight: 700;
    font-size: 33px;
    fill: var(--white);
  }
  .icon { fill: none; stroke: var(--white); stroke-width: 1.6; }
</style>
</head>
<body>
<svg class="billboard" viewBox="0 0 1144 381" xmlns="http://www.w3.org/2000/svg">
  <defs>
    <linearGradient id="photoTone" x1="0" y1="0" x2="0.8" y2="1">
      <stop offset="0" stop-color="#d2d2d2"/>
      <stop offset="0.35" stop-color="#8a8a8a"/>
      <stop offset="0.7" stop-color="#3a3a3a"/>
      <stop offset="1" stop-color="#111111"/>
    </linearGradient>
  </defs>

  <rect class="board-bg" x="0" y="0" width="1144" height="381"/>

  <!-- Right side decoration -->
  <polygon class="deco-darker" points="1021,0 1144,0 1144,200"/>
  <path class="deco-dark" d="M874,0 A29,29 0 0 0 932,0 Z"/>
  <polygon class="deco-dark" points="1031,84 1095,197 982,197"/>
  <line class="deco-line" x1="971" y1="172" x2="1037" y2="35"/>
  <line class="deco-line" x1="1105" y1="123" x2="1144" y2="193"/>
  <circle class="deco-ring" cx="851" cy="140" r="18"/>
  <circle class="deco-dark" cx="892" cy="169" r="11"/>

  <!-- Photo area -->
  <polygon points="0,0 436,0 634,381 0,381" fill="url(#photoTone)"
           role="img" aria-label="Black and white photo of a pickup truck with a raised dump trailer bed"/>
  <polygon class="divider" points="436,0 446,0 644,381 634,381"/>

  <!-- Brand name -->
  <text class="brand-name" x="520" y="86">Keystone</text>
  <text class="brand-name" x="546" y="142">Haulers</text>

  <!-- Service tagline -->
  <text class="tagline" x="29" y="296">Residential &amp; Commercial</text>
  <text class="tagline" x="29" y="353">Dumpster Rentals</text>

  <!-- Offer -->
  <text class="lead" x="574" y="215">Also have</text>
  <text x="606" y="267"><tspan class="sizes">16/20/30</tspan><tspan class="lead" dx="8">yard dumpsters!</tspan></text>

  <!-- Contact band -->
  <rect class="rule" x="598" y="302" width="242" height="4"/>
  <polygon class="contact-band" points="601,310 1144,310 1144,353 616,353"/>

  <g transform="translate(645,331)">
    <circle class="icon" cx="0" cy="0" r="9"/>
    <ellipse class="icon" cx="0" cy="0" rx="4" ry="9"/>
    <line class="icon" x1="-9" y1="0" x2="9" y2="0"/>
  </g>
  <text class="contact-web" x="663" y="339" textLength="212" lengthAdjust="spacingAndGlyphs">keystonehaulers-example.com</text>

  <path class="icon" transform="translate(893,318)" stroke-width="2"
        d="M4,2 L8,2 L10,8 L7,10 Q10,16 15,19 L17,16 L23,18 L23,22 Q22,25 18,24 Q6,21 2,8 Q1,3 4,2 Z"/>
  <text class="contact-phone" x="928" y="344">555-201-4387</text>
</svg>
</body>
</html>
```